Tervane Electronic Security Web Site

We need a web site for our new company based in Sydney Australia.
We specialize in consulting supplying and installing electronic security systems. These include CCTV, Access control, Alarms, Intercom and Network cabling.
We pride our selves in giving our customers peace of mind giving back security and freedom to our customers. We pride in customer service quality products and expertise with and we do the job as though it is for our personal friends and family.
We need to be able to edit web site contents and update information.

```html
<!DOCTYPE html>
<html lang="en">
<head>
<meta charset="utf-8">
<title>Tervane Electronic Security</title>
<link href="https://fonts.googleapis.com/css2?family=Raleway:wght@400;500;600;700&family=Open+Sans:wght@400;600&display=swap" rel="stylesheet">
<style>
:root{
  --blue:#1252b8;
  --blue-dark:#0d3f94;
  --link-light:#4d86e0;
  --page:#ebebeb;
  --card:#ffffff;
  --ink:#333333;
  --muted:#666666;
  --line:#e3e3e3;
  --nav:#ececec;
  --footer:#232323;
  --footer-bar:#2c2c2c;
  --footer-text:#c9c9c9;
}
*{box-sizing:border-box;margin:0;padding:0}
html,body{width:770px;height:1200px;overflow:hidden;background:var(--page)}
body{font-family:"Open Sans",sans-serif;color:var(--ink)}
.site{position:relative;width:802px;height:1250px;transform:scale(0.96);transform-origin:0 0}
.abs{position:absolute}
/* header */
.header{left:62px;top:15px;width:678px;height:70px;background:var(--card);box-shadow:0 1px 2px rgba(0,0,0,.12)}
.brand{left:40px;top:10px}
.brand-mark{position:absolute;left:0;top:4px;width:26px;height:26px;background:var(--blue);border-radius:50%}
.brand-name{position:absolute;left:34px;top:4px;font-family:"Raleway",sans-serif;font-size:15px;color:#2a2a2a;white-space:nowrap}
.brand-tag{position:absolute;left:34px;top:24px;font-family:"Raleway",sans-serif;font-size:10px;color:var(--blue);white-space:nowrap}
.callus{left:490px;top:6px;font-size:9px;color:#333;font-weight:600;display:flex;align-items:center;gap:4px}
.social{left:593px;top:5px;display:flex;gap:3px}
.social span{width:11px;height:11px;border-radius:50%;background:var(--blue)}
.nav{left:209px;top:25px;display:flex;gap:3px}
.nav a{height:35px;line-height:35px;padding:0;text-align:center;background:var(--nav);font-family:"Raleway",sans-serif;font-size:10px;color:#444;text-decoration:none}
.nav a.active{background:var(--blue);color:#fff}
.dropdown{left:397px;top:78px;width:112px;background:#fff;box-shadow:0 2px 6px rgba(0,0,0,.18);z-index:5}
.dropdown li{list-style:none;height:24px;line-height:24px;padding-left:10px;font-size:8px;color:#444;border-bottom:1px solid #eee}
.dropdown li::before{content:"›";margin-right:7px;font-weight:700}
/* hero */
.hero{left:62px;top:95px;width:678px;height:270px;background:linear-gradient(90deg,#d9d5cf 0%,#efe9e2 35%,#e8dcd0 55%,#c8b8a8 72%,#22304d 78%,#1c2740 100%)}
.hero-arrow{width:17px;height:62px;top:99px;background:rgba(40,40,40,.8);display:flex;align-items:center;justify-content:center}
.hero-title{left:83px;top:128px;font-family:"Raleway",sans-serif;font-weight:700;font-size:19px;line-height:25px;color:#222;letter-spacing:.3px}
.hero-text{left:83px;top:185px;width:305px;font-size:7.5px;line-height:12px;color:#333}
.btn{display:inline-block;background:var(--blue);color:#fff;font-family:"Raleway",sans-serif;font-weight:700;font-size:8px;padding:5px 7px;border-bottom:2px solid var(--blue-dark);border-radius:2px}
/* main */
.main{left:62px;top:373px;width:678px;height:552px;background:var(--card);border-top:3px solid var(--blue);box-shadow:0 1px 2px rgba(0,0,0,.1)}
.service{top:30px;width:200px}
.service-icon{position:absolute;left:0;top:0;width:27px;height:27px;border-radius:50%;border:1px solid #ccc;background:#fff}
.service-icon.on{background:var(--blue);border-color:var(--blue)}
.service h3{position:absolute;left:39px;top:3px;font-family:"Raleway",sans-serif;font-weight:500;font-size:10px;letter-spacing:.3px;color:#555}
.service h3.on{color:var(--blue);font-weight:600}
.service p{position:absolute;left:39px;top:23px;width:155px;font-size:7px;line-height:11.5px;color:#666}
.service a{position:absolute;left:39px;top:78px;font-size:7.5px;color:var(--blue);text-decoration:none}
.section-title{font-family:"Raleway",sans-serif;font-size:11px;color:#333}
.rule{height:1px;border-top:1px dashed #ddd}
.rule::before{content:"";display:block;width:19px;height:2px;background:#999;margin-top:-2px}
.clients{left:23px;top:185px;width:632px;display:grid;grid-template-columns:repeat(4,156px);grid-auto-rows:91px;gap:2px}
.client{border:1px solid var(--line);display:flex;align-items:center;justify-content:center;gap:6px;font-family:"Raleway",sans-serif;font-weight:600;font-size:12px;color:#555}
.client i{width:10px;height:10px;border-radius:50%;background:#999;display:block}
.client.feature{background:var(--blue);border-color:var(--blue);display:block;padding:14px 15px;color:#fff;font-weight:400}
.client.feature b{display:block;font-weight:400;font-size:8.5px;padding-bottom:5px;border-bottom:1px solid rgba(255,255,255,.6);margin-bottom:5px}
.client.feature span{font-size:7px;line-height:10.5px;font-family:"Open Sans",sans-serif;display:block}
.team-photo{left:26px;top:430px;width:118px;height:88px;background:linear-gradient(180deg,#f1f1f1 0%,#d8d4d0 40%,#2f2f35 75%,#222 100%)}
.who-text{left:159px;top:429px;width:260px;font-size:7px;line-height:12px;color:#444}
.tabs{left:461px;top:427px;display:flex;gap:2px}
.tabs span{font-size:7.5px;padding:6px 11px;border:1px solid #ddd;background:#eee;color:#444}
.tabs span.on{background:#fff;border-bottom-color:#fff}
.tab-panel{left:461px;top:447px;width:193px;height:79px;border:1px solid #e5e5e5}
.tab-panel p{position:absolute;left:8px;top:12px;width:118px;font-size:7px;line-height:11px;color:#444}
.product-photo{position:absolute;left:130px;top:14px;width:55px;height:42px;background:linear-gradient(135deg,#e6e6e6,#a9a9a9)}
/* footer */
.footer{left:62px;top:938px;width:678px;height:248px;background:var(--footer);border-top:3px solid var(--blue)}
.footer h4{font-family:"Raleway",sans-serif;font-weight:500;font-size:10.5px;color:#e5e5e5}
.footer .frule{height:3px;background:#3a3a3a}
.sectors li{list-style:none;height:22px;line-height:22px;font-size:7.5px;color:var(--footer-text);border-bottom:1px solid #2f2f2f}
.sectors li.on{color:var(--link-light)}
.news{height:52px;border-bottom:1px dashed #3a3a3a;position:relative}
.news .thumb{position:absolute;left:0;top:6px;width:30px;height:30px;border:2px solid #444;background:linear-gradient(135deg,#9aa6b8,#55606f)}
.news .t{position:absolute;left:37px;top:10px;font-size:7.5px;color:var(--footer-text)}
.news .t.on{color:var(--link-light)}
.news .d{position:absolute;left:37px;top:21px;font-size:7.5px;color:#e0e0e0}
.quote{left:461px;top:68px;width:192px;height:122px;background:#2b2b2b}
.quote p{position:absolute;left:11px;top:11px;width:172px;font-size:7px;line-height:12px;color:#b5b5b5}
.reviewer{position:absolute;left:0;bottom:0;width:100%;height:50px;background:#333}
.reviewer .avatar{position:absolute;left:13px;top:8px;width:32px;height:32px;border-radius:50%;background:radial-gradient(circle,#e9c9a8,#8a6243)}
.reviewer .name{position:absolute;left:61px;top:12px;font-size:8px;color:#ddd;font-weight:600}
.reviewer .role{position:absolute;left:61px;top:26px;font-size:6px;color:#888;white-space:nowrap}
.footer-bar{left:62px;top:1187px;width:678px;height:33px;background:var(--footer-bar);display:flex;align-items:center;justify-content:center}
.footer-bar span{padding:0 18px;border-left:1px solid #555;font-size:8.5px;color:#dddddd}
.footer-bar span:first-child{border-left:0}
.copyright{left:0;top:1230px;width:802px;text-align:center;font-size:7px;color:#666}
</style>
</head>
<body>
<div class="site">

  <header class="header abs">
    <div class="brand abs">
      <span class="brand-mark"></span>
      <span class="brand-name">Tervane</span>
      <span class="brand-tag">Electronic Security</span>
    </div>
    <div class="callus abs">
      <svg width="8" height="8" viewBox="0 0 10 10"><path d="M2 1l2 2-1 1.5a6 6 0 0 0 2.5 2.5L7 6l2 2-1.5 1.5C4 9 1 6 .5 2.5z" fill="#333"/></svg>
      Call Us: 9900412378
    </div>
    <div class="social abs"><span></span><span></span><span></span><span></span></div>
    <nav class="nav abs">
      <a class="active" style="width:60px">HOME</a>
      <a style="width:60px">SERVICES</a>
      <a class="active" style="width:62px">PRODUCTS</a>
      <a style="width:60px">ABOUT US</a>
      <a style="width:60px">SECTORS</a>
      <a style="width:60px">CAREER</a>
      <a style="width:66px">CONTACT US</a>
    </nav>
  </header>

  <ul class="dropdown abs">
    <li>CC TV</li><li>Access control</li><li>Alarms</li><li>Intercom</li><li style="border-bottom:0">Network cabling</li>
  </ul>

  <section class="hero abs" role="img" aria-label="Security camera on a wall beside a guard speaking into a radio, houses blurred behind">
    <div class="hero-arrow abs" style="left:0">
      <svg width="8" height="10" viewBox="0 0 8 10"><path d="M6 1L2 5l4 4" stroke="#fff" stroke-width="2" fill="none"/></svg>
    </div>
    <div class="hero-arrow abs" style="right:0">
      <svg width="8" height="10" viewBox="0 0 8 10"><path d="M2 1l4 4-4 4" stroke="#fff" stroke-width="2" fill="none"/></svg>
    </div>
    <h1 class="hero-title abs">WE PROVIDE SECURITY AND<br>FREEDOM TO OUR CUSTOMERS</h1>
    <p class="hero-text abs">Lorem ipsum dolor sit amet, consectetur adipiscing elit, sed do eiusmod tempor incididunt ut labore et dolore magna aliqua. Ut enim ad minim veniam, quis nostrud exercitation ullamco laboris ...</p>
    <span class="btn abs" style="left:83px;top:229px">Learn More</span>
  </section>

  <main class="main abs">
    <div class="service abs" style="left:23px">
      <span class="service-icon on"></span>
      <h3 class="on">CONSULTING</h3>
      <p>Excepteur sint occaecat cupidatat non proident, sunt in culpa qui officia deserunt mollit anim id est laborum.  Ut enim ad minim veniam ...</p>
      <a>Learn More</a>
    </div>
    <div class="service abs" style="left:242px">
      <span class="service-icon"></span>
      <h3>SUPPLYING</h3>
      <p>Sed ut perspiciatis unde omnis iste natus error sit voluptatem accusantium doloremque laudantium, totam rem aperiam, eaque ipsa quae ab illo ...</p>
      <a>Learn More</a>
    </div>
    <div class="service abs" style="left:461px">
      <span class="service-icon"></span>
      <h3>INSTALLING</h3>
      <p>Nemo enim ipsam voluptatem quia voluptas sit aspernatur aut odit aut fugit, sed quia consequuntur magni dolores eos qui ratione voluptatem sequi nesciunt ...</p>
      <a>Learn More</a>
    </div>

    <h2 class="section-title abs" style="left:23px;top:148px">Clients</h2>
    <div class="rule abs" style="left:23px;top:171px;width:632px"></div>
    <div class="clients abs">
      <div class="client feature"><b>Kestrel Hearing</b><span>Quis autem vel eum iure qui in ea voluptate velit esse quam.</span></div>
      <div class="client">Harlow &amp; Finch</div>
      <div class="client" style="color:#1c3a8c">Everwyn</div>
      <div class="client" style="color:#111">Nimbuscore</div>
      <div class="client" style="color:#c8161d">Bright Kite</div>
      <div class="client" style="color:#c8161d">St. Aldric</div>
      <div class="client" style="color:#111">Marlow James</div>
      <div class="client"><i style="background:#3a7fd0"></i>Carrington Telecom</div>
    </div>

    <h2 class="section-title abs" style="left:23px;top:387px">Who We Are</h2>
    <div class="rule abs" style="left:23px;top:409px;width:413px"></div>
    <div class="team-photo abs" role="img" aria-label="Group of smiling business people in suits"></div>
    <p class="who-text abs">We pride our selves in giving our customers peace of mind giving back security and freedom to our customers. We pride in customer service quality products and expertise with and we do the job as though it is for our personal friends and family.</p>
    <span class="btn abs" style="left:160px;top:490px">Leran More</span>

    <h2 class="section-title abs" style="left:461px;top:387px">Products</h2>
    <div class="rule abs" style="left:461px;top:409px;width:193px"></div>
    <div class="tabs abs"><span class="on">CC TV</span><span>Intercom</span></div>
    <div class="tab-panel abs">
      <p>Molestias excepturi sint occaecati cupiditate non provident, similique sunt in culpa qui officia deserunt mollitia animi.</p>
      <div class="product-photo" role="img" aria-label="Bullet security camera"></div>
    </div>
  </main>

  <footer class="footer abs">
    <div class="abs" style="left:24px;top:30px;width:192px">
      <h4>Security for Sectors</h4>
      <div class="frule" style="margin-top:9px;margin-bottom:6px"></div>
      <ul class="sectors">
        <li class="on">Government</li><li>Education</li><li>Aviation</li><li>Health</li><li>Events</li><li>Industries</li><li style="border:0">Properties</li>
      </ul>
    </div>
    <div class="abs" style="left:242px;top:30px;width:192px">
      <h4>Latest News</h4>
      <div class="frule" style="margin-top:9px;margin-bottom:6px"></div>
      <div class="news"><span class="thumb"></span><span class="t on">Nemo Enim Ipsam Voluptatem</span><span class="d">October 22, 2013</span></div>
      <div class="news"><span class="thumb"></span><span class="t">Sed Quia Non Numquam Eius</span><span class="d">October 04, 2013</span></div>
      <div class="news" style="border:0"><span class="thumb"></span><span class="t">Sed Ut Perspiciatis Unde Omnis</span><span class="d">September 15, 2013</span></div>
    </div>
    <div class="abs" style="left:461px;top:30px;width:192px">
      <h4>Customer Feedback</h4>
      <svg class="abs" style="right:0;top:2px" width="18" height="8" viewBox="0 0 18 8"><path d="M4 1L1 4l3 3M14 1l3 3-3 3" stroke="#777" fill="none"/></svg>
      <div class="frule" style="margin-top:9px"></div>
    </div>
    <div class="quote abs">
      <p>Duis aute irure dolor in reprehenderit in voluptate velit esse cillum dolore eu fugiat nulla pariatur. Excepteur sint occaecat cupidatat non proident, sunt in culpa qui officia...</p>
      <div class="reviewer">
        <div class="avatar" role="img" aria-label="Customer portrait"></div>
        <b class="name">Maren Holt</b>
        <span class="role">CEO, Lorem Ipsum Industry</span>
      </div>
      <svg class="abs" style="left:28px;bottom:-10px" width="12" height="10" viewBox="0 0 12 10"><path d="M0 0h12L0 10z" fill="#333"/></svg>
    </div>
  </footer>

  <div class="footer-bar abs"><span>Home</span><span>About Us</span><span>Blog</span><span>Career</span><span>Contact Us</span></div>
  <p class="copyright abs">Copyright 2014. Tervane Electronic Security. All Rights Reserved.</p>
</div>
</body>
</html>
```